IT Company based on Biology Business Needs a Business Card Design

We need a business card design for a new company called 'Lumen CELL'. We develop the machine learning solutions especially focused on deep learning algorithms for biology industry. Our initial product is a vision detection on biological images to help doctors diagnose the symptoms. We would like to see designs that use the color green.

Industry/Entity Type

Business

```html
<!DOCTYPE html>
<html lang="en">
<head>
<meta charset="utf-8">
<title>Lumen CELL – Business Card</title>
<link href="https://fonts.googleapis.com/css2?family=Source+Sans+3:wght@400;600&display=swap" rel="stylesheet">
<style>
  :root {
    --backdrop: #000000;
    --card-light: #f3f3f3;
    --brand-green: #7bc143;
    --brand-green-soft: #72b63d;
    --deep-green: #1c8a3e;
    --text-dark: #3a3a3a;
    --white: #ffffff;
  }
  html, body {
    margin: 0;
    padding: 0;
    width: 1200px;
    height: 900px;
    overflow: hidden;
    background: var(--backdrop);
    font-family: "Source Sans 3", "Myriad Pro", Arial, sans-serif;
  }
  .canvas {
    position: relative;
    width: 1200px;
    height: 900px;
  }
  .card {
    position: absolute;
    top: 200px;
    width: 310px;
    height: 502px;
    overflow: hidden;
  }
  .card-front {
    left: 265px;
    background: var(--card-light);
    border-radius: 62px 0 62px 0;
  }
  .card-back {
    left: 641px;
    background: var(--brand-green);
    border-radius: 0 62px 0 62px;
  }
  .brand {
    position: absolute;
    left: 32px;
    top: 66px;
    display: flex;
    align-items: center;
    gap: 10px;
  }
  .brand-dot {
    width: 16px;
    height: 16px;
    border-radius: 50%;
    background: var(--deep-green);
  }
  .brand-name {
    font-size: 40px;
    font-weight: 600;
    letter-spacing: -1px;
    color: var(--brand-green);
    line-height: 1;
  }
  .contact {
    position: absolute;
    left: 27px;
    top: 326px;
    color: var(--text-dark);
    font-size: 14px;
    line-height: 16px;
  }
  .person-name {
    margin: 0;
    font-size: 18px;
    font-weight: 600;
    color: var(--deep-green);
    line-height: 22px;
  }
  .person-role {
    margin: 3px 0 0;
  }
  .address {
    margin: 19px 0 0;
    font-style: normal;
  }
  .contact-list {
    list-style: none;
    margin: 11px 0 0;
    padding: 0;
  }
  .contact-list li {
    display: flex;
    align-items: center;
    gap: 6px;
    margin-bottom: 3px;
  }
  .contact-icon {
    width: 10px;
    height: 10px;
    fill: var(--deep-green);
  }
  .back-pattern {
    position: absolute;
    inset: 0;
    background: linear-gradient(160deg, var(--brand-green) 0%, var(--brand-green-soft) 100%);
  }
  .back-brand {
    position: absolute;
    left: 0;
    right: 0;
    top: 396px;
    text-align: center;
    font-size: 46px;
    font-weight: 600;
    letter-spacing: -1px;
    color: var(--white);
    line-height: 1;
  }
</style>
</head>
<body>
<main class="canvas">
  <section class="card card-front">
    <div class="brand">
      <span class="brand-dot"></span>
      <span class="brand-name">Lumen CELL</span>
    </div>
    <div class="contact">
      <p class="person-name">MARA ELLISON</p>
      <p class="person-role">Managing Director</p>
      <address class="address">1234, Address Goes Here<br>Country Name, 123456</address>
      <ul class="contact-list">
        <li>
          <svg class="contact-icon" viewBox="0 0 10 10" aria-hidden="true">
            <path d="M0 3.5 Q5 0 10 3.5 L8.5 5 L7 3.8 L7 3 Q5 2.4 3 3 L3 3.8 L1.5 5 Z M2.5 5.5 L7.5 5.5 L9 9.5 L1 9.5 Z"/>
          </svg>
          <span>555-014-2290</span>
        </li>
        <li>
          <svg class="contact-icon" viewBox="0 0 10 10" aria-hidden="true">
            <path d="M0 1.5 H10 V8.5 H0 Z" />
            <path d="M0.5 2 L5 5.5 L9.5 2" fill="none" stroke="#f3f3f3" stroke-width="1"/>
          </svg>
          <span>hello@lumencell.example</span>
        </li>
      </ul>
    </div>
  </section>

  <section class="card card-back">
    <div class="back-pattern" role="img" aria-label="Faint darker green molecular dots and bars pattern"></div>
    <p class="back-brand">Lumen CELL</p>
  </section>
</main>
</body>
</html>
```